Business Card Design

We are a commercial real estate brokerage in San Francisco, leasing office buildings downtown.
I would like a clean, elegant look. Simple but powerful .

Industry/Entity Type

Business

Contact Information for Business Card

Colin Farrow
lic# 07281549
415.555.0172
colin@tarvo-commercial.example
tarvo-commercial.example

```html
<!DOCTYPE html>
<html lang="en">
<head>
<meta charset="utf-8">
<title>Tarvo Commercial — Business Card</title>
<link rel="stylesheet" href="https://fonts.googleapis.com/css2?family=Source+Sans+3:ital,wght@0,400;0,600;1,400&family=Jost:wght@600&display=swap">
<style>
  :root {
    --page-bg: #9b9b9b;
    --card-bg: #e9e9ed;
    --band-dark: #2d2d2e;
    --band-blue: #63718f;
    --accent: #8592b0;
    --text-light: #e4e4e8;
    --icon: #9aa3b8;
    --skyline-top: #5a5a5e;
    --skyline-bottom: #3a3a3c;
    --mark-grey: #4a4a4c;
  }
  * { box-sizing: border-box; margin: 0; padding: 0; }
  html, body { width: 1105px; height: 1200px; overflow: hidden; }
  body {
    background: var(--page-bg);
    position: relative;
    font-family: "Source Sans 3", "Myriad Pro", sans-serif;
  }
  .card {
    position: absolute;
    left: 182px;
    width: 746px;
    height: 427px;
    background: var(--card-bg);
    overflow: hidden;
  }
  .card--front { top: 119px; }
  .card--back { top: 635px; }

  .skyline {
    position: absolute;
    left: 239px;
    top: 33px;
    width: 276px;
    height: 187px;
    background: linear-gradient(180deg, var(--skyline-top), var(--skyline-bottom));
  }
  .contact-band {
    position: absolute;
    left: 0; top: 220px;
    width: 100%; height: 131px;
    background: var(--band-dark);
  }
  .agent {
    position: absolute;
    right: 448px;
    top: 35px;
    text-align: right;
  }
  .agent__name {
    color: var(--accent);
    font-size: 26px;
    font-weight: 600;
    line-height: 1.1;
  }
  .agent__license {
    color: var(--text-light);
    font-size: 20px;
    line-height: 1.1;
    margin-top: 6px;
  }
  .contact-list {
    position: absolute;
    left: 327px;
    top: 24px;
    list-style: none;
  }
  .contact-list li {
    display: flex;
    align-items: center;
    height: 29px;
    color: var(--text-light);
    font-size: 19px;
  }
  .contact-list svg {
    width: 18px; height: 18px;
    margin-right: 17px;
    fill: var(--icon);
    flex: none;
  }
  .tagline-band {
    position: absolute;
    left: 0; top: 351px;
    width: 100%; height: 76px;
    background: var(--band-blue);
    display: flex;
    align-items: center;
    justify-content: center;
  }
  .tagline {
    color: var(--text-light);
    font-style: italic;
    font-size: 19px;
    line-height: 1.35;
    text-align: center;
  }

  .brand {
    position: absolute;
    left: 0; top: 0;
    width: 100%; height: 100%;
    display: flex;
    align-items: center;
    justify-content: center;
    gap: 22px;
  }
  .brand__square {
    width: 54px; height: 54px;
    background: var(--mark-grey);
  }
  .brand__name {
    font-family: "Jost", "Futura", sans-serif;
    font-weight: 600;
    font-size: 44px;
    letter-spacing: 1px;
    color: var(--band-blue);
    line-height: 1;
  }
</style>
</head>
<body>
  <section class="card card--front">
    <div class="skyline" role="img" aria-label="Illustration of a downtown skyline of office towers"></div>
    <div class="contact-band">
      <div class="agent">
        <p class="agent__name">Colin Farrow</p>
        <p class="agent__license">lic# 07281549</p>
      </div>
      <ul class="contact-list">
        <li>
          <svg viewBox="0 0 24 24" aria-hidden="true"><path d="M6.6 10.8a15.1 15.1 0 0 0 6.6 6.6l2.2-2.2a1 1 0 0 1 1-.25 11.4 11.4 0 0 0 3.6.57 1 1 0 0 1 1 1V20a1 1 0 0 1-1 1A17 17 0 0 1 3 4a1 1 0 0 1 1-1h3.5a1 1 0 0 1 1 1c0 1.25.2 2.45.57 3.6a1 1 0 0 1-.25 1z"/></svg>
          415.555.0172
        </li>
        <li>
          <svg viewBox="0 0 24 24" aria-hidden="true"><path d="M2 5h20v14H2z M3.5 6.5 12 12.5l8.5-6" fill="none" stroke="#9aa3b8" stroke-width="2"/><path d="M2 5h20v2l-10 6.5L2 7z"/></svg>
          colin@tarvo-commercial.example
        </li>
        <li>
          <svg viewBox="0 0 24 24" aria-hidden="true"><circle cx="12" cy="12" r="10"/><path d="M2 12h20M12 2c3 3 3 17 0 20M12 2c-3 3-3 17 0 20" fill="none" stroke="#2d2d2e" stroke-width="1.6"/></svg>
          tarvo-commercial.example
        </li>
      </ul>
    </div>
    <div class="tagline-band">
      <p class="tagline">commercial real estate brokerage in San Francisco<br>leasing office buildings downtown.</p>
    </div>
  </section>

  <section class="card card--back">
    <div class="brand">
      <span class="brand__square" aria-hidden="true"></span>
      <span class="brand__name">TARVO COMMERCIAL</span>
    </div>
  </section>
</body>
</html>
```